COVID-19 Accredited CME Impact Infographic

We want an infographic showing how much COVID-19 Continuing Medical Education we have accredited and its impact. Our website is at https://med.halvering.edu/cme/COVID19/education.html The attached document is intended to simply show the elements. You have complete freedom on design. We will be updating the numbers weekly so it is important that we have the files so that we can update it. This can be done in powerpoint, publisher, word, in-design, illustrator. Don't use crazy fonts that we wont have.

Target Market(s)

Internal to Halvering. We just want to show the impact of our work

Industry/Entity Type

Education

Requirements
Must have
• We must be able to update the numbers ourselves.

See attached document for the pieces that we want.

The sizes of the numbers in the attached are based on importance to us.
Nice to have
• Not mandatory but try to use these colors. https://med.halvering.edu/identity/color-palette.html

I was thinking that perhaps the big number could be done in traditional train. Like this: https://www.pictovane.com/image-illustration/flip-board-under-constuction-page-isolated-8803617452

```html
<!DOCTYPE html>
<html lang="en">
<head>
<meta charset="utf-8">
<title>COVID-19 Accredited CME Impact</title>
<link href="https://fonts.googleapis.com/css2?family=Montserrat:wght@500;700&display=swap" rel="stylesheet">
<style>
  :root {
    --page: #fafafa;
    --ink: #1b1416;
    --label: #ffffff;
    --crimson-light: #b0213a;
    --crimson-dark: #7a1628;
    --olive-light: #b2ab7b;
    --olive-dark: #8c864f;
    --coral-light: #d6806c;
    --coral-dark: #bc5747;
    --rose-light: #cf4a63;
    --rose-dark: #ad203a;
    --sand-light: #dcd3b5;
    --sand-dark: #b2aa7b;
    --blush-light: #e6b4a7;
    --blush-dark: #d57f6d;
    --icon-slot: rgba(255,255,255,0.28);
  }
  * { margin: 0; padding: 0; box-sizing: border-box; }
  html, body { width: 1030px; height: 1200px; overflow: hidden; background: var(--page); }
  body { font-family: "Montserrat", Arial, sans-serif; position: relative; }

  .stat { position: absolute; left: 0; width: 1030px; height: 155px; }
  .stat__band { position: absolute; inset: 0; }
  .stat__value, .stat__label { position: absolute; top: 0; height: 155px; display: flex; align-items: center; }
  .stat__value { color: var(--ink); font-weight: 700; letter-spacing: -1px; line-height: 1; }
  .stat__label { color: var(--label); font-weight: 500; font-size: 38px; line-height: 1.2; letter-spacing: 0.3px; white-space: nowrap; }
  .stat__label--center { text-align: center; justify-content: center; }

  .stat--states { top: 98px; }
  .stat--countries { top: 268px; }
  .stat--cme { top: 437px; }
  .stat--live { top: 608px; }
  .stat--activities { top: 778px; }
  .stat--views { top: 947px; }

  .icon-slot { fill: var(--icon-slot); }
</style>
</head>
<body>
<main class="impact">

  <section class="stat stat--states">
    <svg class="stat__band" width="1030" height="155" viewBox="0 0 1030 155">
      <polygon fill="var(--crimson-dark)" points="133,0 898,0 947,77.5 898,155 133,155 87,77.5"/>
      <polygon fill="var(--crimson-light)" points="133,0 247,0 294,77.5 247,155 133,155 87,77.5"/>
      <rect class="icon-slot" x="356" y="22" width="111" height="111" rx="20" role="img" aria-label="Icon of a columned building"/>
    </svg>
    <div class="stat__value" style="left:140px;font-size:74px;">26</div>
    <div class="stat__label" style="left:567px;"># of states</div>
  </section>

  <section class="stat stat--countries">
    <svg class="stat__band" width="1030" height="155" viewBox="0 0 1030 155">
      <polygon fill="var(--olive-dark)" points="133,0 898,0 947,77.5 898,155 133,155 87,77.5"/>
      <polygon fill="var(--olive-light)" points="133,0 322,0 370,77.5 322,155 133,155 87,77.5"/>
      <rect class="icon-slot" x="442" y="30" width="76" height="93" rx="16" role="img" aria-label="Icon of a flag"/>
    </svg>
    <div class="stat__value" style="left:178px;font-size:70px;">12</div>
    <div class="stat__label" style="left:579px;"># of Countries</div>
  </section>

  <section class="stat stat--cme">
    <svg class="stat__band" width="1030" height="155" viewBox="0 0 1030 155">
      <polygon fill="var(--coral-dark)" points="133,0 898,0 947,77.5 898,155 133,155 87,77.5"/>
      <polygon fill="var(--coral-light)" points="133,0 441,0 489,77.5 441,155 133,155 87,77.5"/>
      <rect class="icon-slot" x="517" y="28" width="88" height="100" rx="40" role="img" aria-label="Icon of a learner with a book"/>
    </svg>
    <div class="stat__value" style="left:180px;font-size:78px;">5,879</div>
    <div class="stat__label stat__label--center" style="left:648px;width:240px;"># of CME<br>Learners</div>
  </section>

  <section class="stat stat--live">
    <svg class="stat__band" width="1030" height="155" viewBox="0 0 1030 155">
      <polygon fill="var(--rose-dark)" points="133,0 898,0 947,77.5 898,155 133,155 87,77.5"/>
      <polygon fill="var(--rose-light)" points="133,0 467,0 513,77.5 467,155 133,155 87,77.5"/>
      <rect class="icon-slot" x="147" y="24" width="103" height="106" rx="20" role="img" aria-label="Icon of a person reading"/>
    </svg>
    <div class="stat__value" style="left:268px;font-size:63px;">23,098</div>
    <div class="stat__label" style="left:544px;"># of live Learners</div>
  </section>

  <section class="stat stat--activities">
    <svg class="stat__band" width="1030" height="155" viewBox="0 0 1030 155">
      <polygon fill="var(--sand-dark)" points="133,0 898,0 947,77.5 898,155 133,155 87,77.5"/>
      <polygon fill="var(--sand-light)" points="133,0 533,0 583,77.5 533,155 133,155 87,77.5"/>
      <circle class="icon-slot" cx="221" cy="80" r="57" role="img" aria-label="Icon of a running figure"/>
    </svg>
    <div class="stat__value" style="left:364px;font-size:68px;">23</div>
    <div class="stat__label" style="left:614px;"># of Activities</div>
  </section>

  <section class="stat stat--views">
    <svg class="stat__band" width="1030" height="155" viewBox="0 0 1030 155">
      <polygon fill="var(--blush-dark)" points="133,0 898,0 947,77.5 898,155 133,155 87,77.5"/>
      <polygon fill="var(--blush-light)" points="133,0 614,0 650,77.5 614,155 133,155 87,77.5"/>
      <rect class="icon-slot" x="203" y="31" width="114" height="105" rx="22" role="img" aria-label="Icon of an eye"/>
    </svg>
    <div class="stat__value" style="left:332px;font-size:63px;">1,209,987</div>
    <div class="stat__label stat__label--center" style="left:668px;width:262px;"># of total<br>on-demand<br>views</div>
  </section>

</main>
</body>
</html>
```